Landing Page Side by Side With Dr. Korwell

Hello!

I am looking for a high converting Landing Page for a One on One Coaching program that Dr. Korwell is releasing. I created a moch up for content but the spacing and graphics are not cohesive. I like the medical look at the top of the first page - the image is the graphic "Get Side BY Side Support from Dr. Korwell.
Please let me know if you have any questions!
Thank you!

```html
<!DOCTYPE html>
<html lang="en">
<head>
<meta charset="utf-8">
<title>Side by Side With Dr. Korwell</title>
<link rel="stylesheet" href="https://fonts.googleapis.com/css2?family=Oswald:wght@400;500&family=Open+Sans:wght@400;600&display=swap">
<style>
:root{
  --navy:#1f2a7a;
  --navy-deep:#17206a;
  --navy-mid:#2b3a92;
  --green:#5b9f2b;
  --green-light:#7cb83a;
  --orange:#f7941d;
  --orange-dark:#ef7f12;
  --ink:#3c3c3c;
  --muted:#6b6b6b;
  --line:#d9d9de;
  --white:#ffffff;
}
*{margin:0;padding:0;box-sizing:border-box}
html,body{width:1200px;height:2486px;overflow:hidden;background:var(--white)}
body{position:relative;font-family:"Open Sans",Arial,sans-serif;color:var(--ink)}
.heading{font-family:"Oswald",Arial Narrow,sans-serif;font-weight:400;text-transform:uppercase;letter-spacing:.5px}
.abs{position:absolute}

/* hero */
.hero{position:absolute;left:0;top:0;width:1200px;height:655px;overflow:hidden;
  background:linear-gradient(105deg,var(--green) 0%,#3f7a4a 28%,var(--navy-mid) 55%,var(--navy) 100%)}
.brand{position:absolute;left:190px;top:28px;font-family:"Oswald",sans-serif;font-weight:500;font-size:46px;color:var(--navy);letter-spacing:-.5px}
.menu{position:absolute;left:975px;top:40px;width:44px}
.menu span{display:block;height:4px;background:var(--white);border-radius:2px;margin-bottom:8px}
.hero-photo{position:absolute;left:174px;top:108px;width:456px;height:540px;border-radius:200px 200px 0 0;
  background:linear-gradient(180deg,#c9b7a6 0%,#eef0f4 45%,#dfe3ea 100%)}
.hero-title{position:absolute;left:633px;top:202px;font-size:62px;line-height:1.03;color:var(--white)}
.hero-sub{position:absolute;left:640px;top:342px;font-size:26px;line-height:1.3;color:var(--white)}
.hero-wave{position:absolute;left:0;top:560px}

/* intro */
.intro-box{position:absolute;left:176px;top:724px;width:465px;height:327px;border:1.5px solid #7c84bd}
.intro-title{position:absolute;left:220px;top:772px;font-size:31px;line-height:1.12;color:#1c1c1c}
.intro-text{position:absolute;left:218px;top:856px;width:320px;font-size:18px;line-height:1.5;color:var(--muted)}
.video{position:absolute;left:582px;top:757px;width:426px;height:262px;
  background:linear-gradient(180deg,#6c6c6c 0%,#4a4a4a 100%);box-shadow:0 8px 18px rgba(0,0,0,.3)}
.video-person{position:absolute;left:130px;top:0;width:170px;height:262px;border-radius:80px 80px 0 0;
  background:linear-gradient(180deg,#5a4a42 0%,#262a38 60%,#1f2330 100%)}

/* commitment */
.commit{position:absolute;left:0;top:1085px;width:1200px;height:580px;overflow:hidden;background:var(--navy)}
.commit-photo{position:absolute;left:0;top:0;width:760px;height:580px;
  background:linear-gradient(90deg,#d7dcd3 0%,#dcc3cf 40%,#9aa0c0 65%,rgba(31,42,122,0) 100%)}
.commit-fade{position:absolute;left:420px;top:0;width:500px;height:580px;
  background:linear-gradient(90deg,rgba(31,42,122,0) 0%,rgba(31,42,122,.85) 55%,var(--navy) 100%)}
.commit-title{position:absolute;left:605px;top:1236px;font-size:31px;line-height:1.15;color:var(--white)}
.benefits{position:absolute;left:610px;top:1332px;width:420px;display:grid;grid-template-columns:232px 200px;row-gap:13px;list-style:none}
.benefits li{display:flex;align-items:center;gap:12px;color:var(--white);font-size:16px}
.benefits svg{flex:none}
.btn{position:absolute;display:flex;align-items:center;justify-content:center;background:var(--orange);
  color:var(--white);font-family:"Oswald",sans-serif;text-transform:uppercase;border-radius:30px;
  box-shadow:0 3px 0 var(--orange-dark)}
.btn-commit{left:615px;top:1496px;width:404px;height:48px;font-size:15px}

/* fence */
.fence{position:absolute;left:406px;top:1703px;width:386px;height:52px;border:1.5px solid #9aa0c6;border-radius:26px;
  display:flex;align-items:center;justify-content:center;font-size:19px;color:#333}
.fence a{color:var(--orange);text-decoration:none;margin-left:6px}
.pillars-title{position:absolute;left:0;top:1788px;width:1200px;text-align:center;font-size:24.5px;line-height:1.32;color:var(--navy)}

/* pillar cards */
.card{position:absolute;top:1916px;width:262px;height:242px;background:var(--white);
  border:1px solid var(--line);border-top:4px solid var(--navy);box-shadow:0 2px 4px rgba(0,0,0,.08)}
.card-badge{position:absolute;left:94px;top:-35px;width:74px;height:74px;border-radius:50%;border:3px solid var(--navy);background:var(--white)}
.card-title{position:absolute;left:0;top:64px;width:100%;text-align:center;font-size:16px;color:#222}
.card-text{position:absolute;left:26px;top:90px;width:210px;text-align:center;font-size:12px;line-height:1.5;color:#777}
.arrow{position:absolute;top:2000px}
.btn-ready{left:461px;top:2196px;width:283px;height:41px;font-size:14px}

/* footer */
.footer{position:absolute;left:0;top:2280px;width:1200px;height:206px}
.copyright{position:absolute;left:0;top:2380px;width:1200px;text-align:center;font-size:11px;letter-spacing:.6px;color:var(--white)}
.social{position:absolute;left:526px;top:2406px;display:flex;gap:6px;list-style:none}
.social li{width:32px;height:32px;border:1.5px solid var(--white);border-radius:50%}
</style>
</head>
<body>

<header class="hero">
  <div class="brand">DR.KORWELL</div>
  <div class="menu" aria-label="Menu"><span></span><span></span><span></span></div>
  <div class="hero-photo" role="img" aria-label="Portrait of Dr. Korwell in a white medical coat, arms crossed"></div>
  <h1 class="hero-title heading">Get Side by<br>Side Support</h1>
  <p class="hero-sub heading">From Dr Korwell<br>Total Wellness Coaching Program</p>
  <svg class="hero-wave" width="1200" height="95" viewBox="0 0 1200 95" aria-hidden="true">
    <path d="M0 30 C250 85 500 95 760 60 C930 38 1080 10 1200 20 L1200 95 L0 95Z" fill="#e6e8ef"/>
    <path d="M0 50 C260 100 520 100 780 75 C950 58 1090 40 1200 48 L1200 95 L0 95Z" fill="#ffffff"/>
  </svg>
</header>

<section>
  <div class="intro-box"></div>
  <h2 class="intro-title heading">Concierge Total Wellness<br>From a Practicing MD!</h2>
  <p class="intro-text">Why wait for a doctors appointment when you can receive one on one care an ongoing basis. Dr. Korwell Currently has a four-month wait list to see him in his practice</p>
  <div class="video">
    <div class="video-person" role="img" aria-label="Video still of Dr. Korwell in a dark suit"></div>
    <svg class="abs" style="left:0;top:0" width="426" height="262" viewBox="0 0 426 262" aria-hidden="true">
      <circle cx="213" cy="131" r="27" fill="none" stroke="#fff" stroke-width="3"/>
      <path d="M205 118 L225 131 L205 144Z" fill="#fff"/>
      <line x1="40" y1="240" x2="408" y2="240" stroke="#d5d5d5" stroke-width="2"/>
      <line x1="40" y1="240" x2="86" y2="240" stroke="#2b2be0" stroke-width="2"/>
      <circle cx="86" cy="240" r="3" fill="#2b2be0"/>
      <circle cx="28" cy="240" r="13" fill="#2b2be0"/>
      <path d="M24 233 L34 240 L24 247Z" fill="#fff"/>
    </svg>
  </div>
</section>

<section class="commit">
  <div class="commit-photo" role="img" aria-label="Smiling woman in a pink top meditating cross-legged in a bright room"></div>
  <div class="commit-fade"></div>
  <svg class="abs" style="left:0;top:0" width="1200" height="580" viewBox="0 0 1200 580" aria-hidden="true">
    <path d="M0 0 L1200 0 L1200 30 C900 80 520 10 200 2 C110 0 40 6 0 12Z" fill="#ffffff"/>
    <path d="M0 12 C40 6 110 0 200 2 C520 10 900 80 1200 30 L1200 36 C900 88 520 26 200 16 C110 14 40 18 0 24Z" fill="var(--green)"/>
    <path d="M0 540 C300 560 700 580 1200 530 L1200 580 L0 580Z" fill="#ffffff"/>
    <path d="M560 575 C800 570 1000 550 1200 518 L1200 532 C1000 560 800 576 600 580Z" fill="var(--green)"/>
  </svg>
</section>
<h2 class="commit-title heading">Make a Commitment<br>to Yourself</h2>
<ul class="benefits">
  <li><svg width="20" height="20" viewBox="0 0 20 20" aria-hidden="true"><circle cx="10" cy="10" r="8" fill="none" stroke="#fff" stroke-width="1.6"/><path d="M6 10.5 L9 13 L14 7" fill="none" stroke="#fff" stroke-width="1.8"/></svg>Lose Weight</li>
  <li><svg width="20" height="20" viewBox="0 0 20 20" aria-hidden="true"><circle cx="10" cy="10" r="8" fill="none" stroke="#fff" stroke-width="1.6"/><path d="M6 10.5 L9 13 L14 7" fill="none" stroke="#fff" stroke-width="1.8"/></svg>Increase Energy</li>
  <li><svg width="20" height="20" viewBox="0 0 20 20" aria-hidden="true"><circle cx="10" cy="10" r="8" fill="none" stroke="#fff" stroke-width="1.6"/><path d="M6 10.5 L9 13 L14 7" fill="none" stroke="#fff" stroke-width="1.8"/></svg>Conquer Mental Illness</li>
  <li><svg width="20" height="20" viewBox="0 0 20 20" aria-hidden="true"><circle cx="10" cy="10" r="8" fill="none" stroke="#fff" stroke-width="1.6"/><path d="M6 10.5 L9 13 L14 7" fill="none" stroke="#fff" stroke-width="1.8"/></svg>Live Joyfully</li>
  <li><svg width="20" height="20" viewBox="0 0 20 20" aria-hidden="true"><circle cx="10" cy="10" r="8" fill="none" stroke="#fff" stroke-width="1.6"/><path d="M6 10.5 L9 13 L14 7" fill="none" stroke="#fff" stroke-width="1.8"/></svg>Build a Better Trip</li>
  <li><svg width="20" height="20" viewBox="0 0 20 20" aria-hidden="true"><circle cx="10" cy="10" r="8" fill="none" stroke="#fff" stroke-width="1.6"/><path d="M6 10.5 L9 13 L14 7" fill="none" stroke="#fff" stroke-width="1.8"/></svg>Cultivate Relationships</li>
  <li><svg width="20" height="20" viewBox="0 0 20 20" aria-hidden="true"><circle cx="10" cy="10" r="8" fill="none" stroke="#fff" stroke-width="1.6"/><path d="M6 10.5 L9 13 L14 7" fill="none" stroke="#fff" stroke-width="1.8"/></svg>Combat Stress &amp; Disease</li>
  <li><svg width="20" height="20" viewBox="0 0 20 20" aria-hidden="true"><circle cx="10" cy="10" r="8" fill="none" stroke="#fff" stroke-width="1.6"/><path d="M6 10.5 L9 13 L14 7" fill="none" stroke="#fff" stroke-width="1.8"/></svg>Clarify Your Purpose</li>
</ul>
<a class="btn btn-commit">Sign Me Up for Side by Side Coaching With Dr. Korwell &nbsp;›</a>

<section>
  <p class="fence">Still on the fence? <a>Learn More</a></p>
  <h2 class="pillars-title heading">Dr. Korwell coaches you one on one in areas based on his five<br>pillar formula for total wellness</h2>

  <svg class="arrow" style="left:138px" width="24" height="50" viewBox="0 0 24 50" aria-hidden="true"><path d="M20 3 L4 25 L20 47" fill="none" stroke="#8a8a8a" stroke-width="2"/></svg>
  <svg class="arrow" style="left:1008px" width="24" height="50" viewBox="0 0 24 50" aria-hidden="true"><path d="M4 3 L20 25 L4 47" fill="none" stroke="#8a8a8a" stroke-width="2"/></svg>

  <article class="card" style="left:176px">
    <div class="card-badge"></div>
    <h3 class="card-title heading">Nutrition</h3>
    <p class="card-text">Learn simple, lasting eating habits that fuel your body, calm inflammation and support healthy digestion, with meal guidance shaped around your tastes, schedule and goals.</p>
  </article>
  <article class="card" style="left:457px">
    <div class="card-badge"></div>
    <h3 class="card-title heading">Movement</h3>
    <p class="card-text">Build strength, balance and stamina through gentle daily activity planned for your level, so moving becomes a habit you enjoy rather than a chore you avoid.</p>
  </article>
  <article class="card" style="left:734px">
    <div class="card-badge"></div>
    <h3 class="card-title heading">Tribe</h3>
    <p class="card-text">Surround yourself with people who lift you up, strengthen the bonds that matter most and discover how real connection supports a longer, happier and healthier life.</p>
  </article>

  <a class="btn btn-ready">Sign Me Up! I Am Ready for Change &nbsp;›</a>
</section>

<footer class="footer">
  <svg class="abs" style="left:0;top:0" width="1200" height="206" viewBox="0 0 1200 206" aria-hidden="true">
    <path d="M0 10 C200 40 480 50 770 8" fill="none" stroke="var(--navy)" stroke-width="4"/>
    <path d="M0 24 C300 60 700 70 1200 30 L1200 206 L0 206Z" fill="var(--navy)"/>
    <path d="M0 24 C300 60 700 70 1200 30 L1200 46 C700 84 300 72 0 40Z" fill="var(--navy-mid)"/>
  </svg>
  <p class="copyright">© 2018 COMPANY NAME &nbsp;ALL RIGHT RESERVED</p>
  <ul class="social" aria-label="Social links"><li></li><li></li><li></li><li></li></ul>
</footer>

</body>
</html>
```